Book Title: THE QUIET LEDGER
Book Sub Title: Notes on forgotten harbours and the keepers who tended their lamps
Vibe: Professional, stylish, trustworthy (high-end men's fashion)
Website (for inspiration): www.velmorandpike.com
Attached: a potential photo to use for the cover, but open to other options (from our website)

```html
<!DOCTYPE html>
<html lang="en">
<head>
<meta charset="utf-8">
<title>The Quiet Ledger – Cover Spread</title>
<link rel="stylesheet" href="https://fonts.googleapis.com/css2?family=Playfair+Display:wght@700;800&family=Outfit:wght@400&display=swap">
<style>
  :root{
    --page:#ffffff;
    --slate:#333d47;
    --slate-deep:#2b343d;
    --gold:#e8cf2a;
    --paper:#eef2f5;
    --ink:#1c2329;
    --photo-light:#d3d9de;
    --photo-mid:#9ba4ac;
    --photo-dark:#3e454c;
    --suit:#2a3038;
  }
  *{margin:0;padding:0;box-sizing:border-box}
  html,body{width:757px;height:1200px;overflow:hidden;background:var(--page)}
  .canvas{position:relative;width:757px;height:1200px;background:var(--page)}
  .spread{position:absolute;left:34px;top:365px;width:690px;height:471px;
    box-shadow:0 4px 14px rgba(0,0,0,.35);background:var(--slate);overflow:hidden}
  .serif{font-family:"Playfair Display",Georgia,serif;font-weight:800;line-height:1}
  .sans{font-family:"Outfit",Arial,sans-serif;font-weight:400}

  /* back cover */
  .back{position:absolute;left:0;top:0;width:322px;height:471px;background:var(--slate)}
  .back .corner-tile{position:absolute;left:0;top:0;width:86px;height:86px;background:var(--paper)}
  .back .title{position:absolute;right:20px;top:46px;text-align:right}
  .back .title .t-small{font-size:17px;color:var(--gold)}
  .back .title .t-big{font-size:32px;color:#fff}
  .back .title .t-last{display:block;font-size:17px;color:var(--gold);margin-top:1px}
  .back .subtitle{position:absolute;left:10px;right:10px;top:217px;text-align:center;
    font-size:10px;line-height:13px;color:#d7dde2}
  .back .photo{position:absolute;left:0;bottom:0;width:322px;height:205px;
    background:
      linear-gradient(180deg,rgba(40,48,56,.35) 0%,rgba(40,48,56,.35) 28%,rgba(0,0,0,0) 28%),
      radial-gradient(ellipse 50px 80px at 48% 55%,rgba(42,48,56,.85) 0%,rgba(42,48,56,0) 100%),
      linear-gradient(90deg,var(--photo-light) 0%,#b4bcc3 50%,#6f7880 72%,#262c33 82%,#1f252b 100%)}

  /* spine */
  .spine-rule{position:absolute;left:322px;top:0;width:2px;height:471px;background:#6b747c}
  .spine{position:absolute;left:324px;top:0;width:45px;height:471px;background:var(--slate-deep)}
  .spine .spine-title{position:absolute;left:50%;top:50%;white-space:nowrap;
    transform:translate(-50%,-50%) rotate(90deg);font-size:21px;letter-spacing:7px;
    color:var(--gold);font-weight:700}

  /* front cover */
  .front{position:absolute;left:369px;top:0;width:321px;height:471px}
  .front .photo{position:absolute;inset:0;
    background:
      radial-gradient(ellipse 60px 120px at 42% 62%,rgba(42,48,56,.9) 0%,rgba(42,48,56,0) 100%),
      radial-gradient(ellipse 70px 90px at 85% 62%,rgba(70,78,86,.55) 0%,rgba(70,78,86,0) 100%),
      radial-gradient(ellipse 40px 55px at 22% 36%,rgba(245,248,250,.8) 0%,rgba(245,248,250,0) 100%),
      radial-gradient(ellipse 30px 45px at 82% 38%,rgba(245,248,250,.7) 0%,rgba(245,248,250,0) 100%),
      linear-gradient(180deg,#c8cfd5 0%,#b9c1c8 35%,#a3acb4 60%,#8f98a0 72%,#bfc6cc 85%,#d4dade 100%)}
  .front .light-bar{position:absolute;top:0;height:230px;background:rgba(255,255,255,.18)}
  .front .bar-a{left:4px;width:22px}
  .front .bar-b{left:32px;width:14px;height:200px}
  .front .bar-c{left:52px;width:30px;height:250px;background:rgba(255,255,255,.12)}
  .front .foot-wash{position:absolute;left:0;right:0;bottom:0;height:86px;background:rgba(235,240,244,.5)}
  .front .title{position:absolute;right:22px;top:14px;text-align:right}
  .front .title .t-small{font-size:28px;color:var(--gold)}
  .front .title .t-big{font-size:52px;color:#fff}
  .front .title .t-last{display:block;font-size:30px;color:var(--gold);margin-top:0}
  .front .subtitle{position:absolute;left:0;width:236px;top:413px;text-align:center;
    font-size:10px;line-height:13px;color:var(--ink)}
  .front .corner-tile{position:absolute;right:0;bottom:0;width:86px;height:86px;background:var(--paper)}
</style>
</head>
<body>
<div class="canvas">
  <div class="spread">
    <section class="back">
      <div class="corner-tile"></div>
      <h2 class="title serif"><span class="t-small">THE </span><span class="t-big">QUIET</span><span class="t-last">LEDGER</span></h2>
      <p class="subtitle sans">Notes On Forgotten Harbours And The Keepers<br>Who Tended Their Lamps.</p>
      <div class="photo" role="img" aria-label="Photo of a single dark jacket hanging on a metal clothes rail in a bare studio"></div>
    </section>

    <div class="spine-rule"></div>
    <section class="spine">
      <span class="spine-title serif">THE QUIET LEDGER</span>
    </section>

    <section class="front">
      <div class="photo" role="img" aria-label="Black and white photo of a man in a dark suit seated on a wooden stool in a loft beside a rail of jackets"></div>
      <div class="light-bar bar-a"></div>
      <div class="light-bar bar-b"></div>
      <div class="light-bar bar-c"></div>
      <div class="foot-wash"></div>
      <h1 class="title serif"><span class="t-small">THE </span><span class="t-big">QUIET</span><span class="t-last">LEDGER</span></h1>
      <p class="subtitle sans">Notes On Forgotten Harbours And The Keepers<br>Who Tended Their Lamps.</p>
      <div class="corner-tile"></div>
    </section>
  </div>
</div>
</body>
</html>
```